Halvern Ditchworks LTD - website for irrigation & Landscape Lighting & Buried service wire

Looking for a website to help promote my business with Irrigation (installation, service, etc) and buried service wire/drainage solutions.

Commercial/Residential

Landscape lighting.

I’ll get photos in the trucks and trailers to upload as well maybe the machine as well.

Target Market(s)

Homeowners who want green grass and beautiful gardens. Beautiful landscape lighting

Industry/Entity Type

Irrigation systems and landscape lighting and buried service wire to homes and offering Drainage soltions.

Coding

Coded - Design and coding required

Number of Pages Required

4 page

Colors
F0912C
F2A743
F7CA91
FBE8D2
FDF5EE

Requirements
Must have
• was hoping to link up my email on halvernditchworks@mailbarn.net with the website if possible.
Nice to have
• Page for Irrigation, page for landscape lighting, page buried service wire & drainage soltions.

```html
<!DOCTYPE html>
<html lang="en">
<head>
<meta charset="utf-8">
<title>Halvern Ditchworks LTD — Irrigation &amp; Landscape Lighting</title>
<link rel="stylesheet" href="https://fonts.googleapis.com/css2?family=Questrial&family=Roboto:wght@300;400;500;700&display=swap">
<style>
:root{
  --orange:#F0912C;
  --orange-2:#F2A743;
  --orange-3:#F7CA91;
  --orange-4:#FBE8D2;
  --cream:#FDF5EE;
  --ink:#1d1d1d;
  --text:#5b5b5b;
  --grey-bg:#f1f1f1;
  --field:#efefef;
  --dark:#1b1b1b;
  --btn-grey:#7a7a7a;
}
*{box-sizing:border-box;margin:0;padding:0}
html,body{width:1200px;height:3222px;overflow:hidden}
body{position:relative;background:#fff;font-family:'Roboto',sans-serif;color:var(--text)}
.abs{position:absolute}
h1,h2,h3,.brand{font-family:'Questrial',sans-serif;font-weight:400;color:var(--ink)}
.btn{position:absolute;display:flex;align-items:center;justify-content:center;font-family:'Roboto',sans-serif;font-weight:700;font-size:15px;border-radius:3px;color:#fff;background:var(--orange)}

/* header */
.topbar{left:338px;top:0;width:862px;height:51px;background:var(--orange);clip-path:polygon(0 0,100% 0,100% 100%,22px 100%)}
.topbar-contact{top:16px;color:#fff;font-size:15px;font-weight:500;display:flex;align-items:center;gap:10px}
.topbar-social{top:18px;right:112px;display:flex;gap:11px}
.topbar-social span{width:15px;height:15px;border-radius:2px;background:#fff;display:block}
.header-line{left:0;top:0;width:338px;height:4px;background:var(--orange)}
.brand{left:110px;top:48px;font-size:25px;color:var(--orange);display:flex;align-items:center;gap:10px}
.brand i{width:20px;height:20px;background:var(--orange);display:block}
.main-nav{top:84px;left:419px;display:flex;gap:38px;font-size:15.5px;color:#777}
.header-rule{left:0;top:128px;width:1200px;height:1px;background:#e6e6e6}

/* hero */
.hero{left:0;top:129px;width:1200px;height:600px;background:linear-gradient(160deg,#2f3a1c 0%,#4b5a25 35%,#6b7a2a 60%,#3a3215 100%)}
.hero h1{left:109px;top:330px;width:520px;font-size:42px;line-height:55px;color:#fff}
.hero-sub{left:107px;top:508px;font-size:21px;font-weight:500;color:#fff}
.btn-outline{background:#fff;color:var(--orange)}

/* estimate form */
.estimate{left:632px;top:564px;width:456px;height:571px;background:#fff;border-radius:6px;box-shadow:0 6px 24px rgba(0,0,0,.08)}
.estimate h2{position:absolute;left:0;width:100%;top:30px;text-align:center;font-size:32px}
.field{position:absolute;left:39px;width:378px;height:51px;background:var(--field);border-radius:2px;font-size:12.5px;color:#666;padding:18px 25px}
.field .caret{position:absolute;right:18px;top:23px;width:0;height:0;border-left:5px solid transparent;border-right:5px solid transparent;border-top:6px solid #555}

/* about */
.about{left:0;top:729px;width:1200px;height:491px;background:var(--grey-bg)}
.about h2{left:110px;top:778px;font-size:38px}
.about-text{left:110px;top:836px;width:470px;font-size:14.5px;line-height:29px;font-weight:300;color:#444}
.about-text p+p{margin-top:29px}

/* services */
.section-title{left:0;width:1200px;text-align:center;font-size:38px}
.section-lead{left:180px;width:840px;text-align:center;font-size:14.5px;line-height:31px;font-weight:300;color:#444}
.service-card{top:1446px;width:236px;height:358px;background:#fff;box-shadow:0 4px 18px rgba(0,0,0,.09);text-align:center}
.service-card h3{margin-top:27px;font-size:19px}
.service-card a{display:block;margin-top:6px;font-size:14.5px;font-weight:500;color:var(--orange);text-decoration:underline}
.service-card .photo{margin:13px auto 0;width:224px;height:150px}
.service-card p{margin:20px 14px 0;font-size:13.5px;line-height:23px;font-weight:300;color:#444}

/* gallery */
.gallery-main{left:111px;top:1972px;width:977px;height:526px;background:radial-gradient(ellipse at 55% 70%,#c8902a 0%,#7a5a2a 25%,#3d4d5e 60%,#2b4570 100%)}
.gallery-side-l{left:0;top:1972px;width:83px;height:526px;background:linear-gradient(180deg,#6b7a4a,#2e5a8a)}
.gallery-side-r{left:1117px;top:1972px;width:83px;height:526px;background:linear-gradient(180deg,#4a6ea0,#9a7a6a)}

/* newsletter */
.subscribe{left:255px;top:2745px;width:686px;height:59px;border-radius:30px;background:#fff;box-shadow:0 4px 16px rgba(0,0,0,.07)}
.subscribe span{position:absolute;left:35px;top:20px;font-size:15px;color:#777}
.subscribe .btn{right:0;top:4px;width:246px;height:51px;border-radius:26px;font-size:17px}

/* footer */
.footer{left:0;top:2909px;width:1200px;height:313px;background:var(--dark)}
.footer .brand{left:0;width:1200px;top:52px;justify-content:center;font-size:28px}
.footer-nav{top:175px;left:0;width:1200px;display:flex;justify-content:center;gap:43px;color:#fff;font-size:16.5px;font-weight:500}
.footer-social{top:220px;left:0;width:1200px;display:flex;justify-content:center;gap:7px}
.footer-social span{width:32px;height:32px;border-radius:50%;background:var(--orange);display:block}
.copyright{top:276px;left:0;width:1200px;text-align:center;color:#fff;font-size:12px}
</style>
</head>
<body>

<header>
  <div class="abs header-line"></div>
  <div class="abs topbar"></div>
  <div class="abs topbar-contact" style="left:388px">
    <svg width="14" height="14" viewBox="0 0 24 24"><path fill="#fff" d="M6.6 10.8a15 15 0 0 0 6.6 6.6l2.2-2.2a1 1 0 0 1 1-.25 11.4 11.4 0 0 0 3.6.57 1 1 0 0 1 1 1V20a1 1 0 0 1-1 1A17 17 0 0 1 3 4a1 1 0 0 1 1-1h3.5a1 1 0 0 1 1 1c0 1.25.2 2.45.57 3.57a1 1 0 0 1-.25 1z"/></svg>
    +1 555 010 2040
  </div>
  <div class="abs topbar-contact" style="left:591px">
    <svg width="16" height="12" viewBox="0 0 16 12"><rect width="16" height="12" rx="1" fill="#fff"/><path d="M1 1l7 5 7-5" stroke="var(--orange)" stroke-width="1.5" fill="none"/></svg>
    halvernditchworks@mailbarn.net
  </div>
  <div class="abs topbar-social"><span></span><span></span><span></span><span></span></div>

  <div class="abs brand"><i></i>Halvern Ditchworks LTD</div>
  <nav class="abs main-nav">
    <span>About Us</span><span>Irrigation Installs</span><span>Service</span><span>Landscape Lighting</span><span>Fiber Optic Installation</span>
  </nav>
  <div class="abs header-rule"></div>
</header>

<section>
  <div class="abs hero" role="img" aria-label="Evening garden with a lit lawn, trees and a bollard landscape light"></div>
  <h1 class="abs" style="left:109px;top:330px;width:520px;font-size:42px;line-height:55px;color:#fff">Homeowners who want green grass and beautiful gardens.</h1>
  <div class="abs hero-sub">Beautiful landscape lighting</div>
  <div class="btn" style="left:108px;top:559px;width:129px;height:43px">Get Started</div>
  <div class="btn btn-outline" style="left:262px;top:559px;width:129px;height:43px">Our Services</div>
</section>

<section>
  <div class="abs about"></div>
  <h2 class="abs" style="left:110px;top:778px;font-size:38px">About Us</h2>
  <div class="abs about-text">
    <p>I must explain to you how all this mistaken idea of denouncing pleasure and praising pain was born and I will give you a complete account of the system, and expound the actual teachings of the great explorer of the truth, the master-builder of human happiness.</p>
    <p>No one rejects, dislikes, or avoids pleasure itself, because it is pleasure, but because those who do not know how to pursue pleasure rationally encounter consequences that are extremely painful. Nor again is there anyone who loves or pursues or desires</p>
  </div>
  <div class="btn" style="left:110px;top:1116px;width:128px;height:43px">Read More</div>
</section>

<form class="abs estimate">
  <h2>Request An Estimate</h2>
  <div class="field" style="top:90px">Full Name</div>
  <div class="field" style="top:158px">Email Address</div>
  <div class="field" style="top:226px">Contact Number</div>
  <div class="field" style="top:295px">Choose The service<span class="caret"></span></div>
  <div class="field" style="top:363px;height:101px">Comments</div>
  <div class="btn" style="left:39px;top:482px;width:378px;height:51px;font-size:16px">Request A Service</div>
</form>

<section>
  <h2 class="abs section-title" style="top:1282px">Our Services</h2>
  <p class="abs section-lead" style="top:1352px">I must explain to you how all this mistaken idea of denouncing pleasure and praising pain was born and I will give you a complete account of the system, and expound the actual teachings of the great explorer of the truth, the master</p>

  <article class="abs service-card" style="left:88px">
    <h3>Commercial Lighting</h3><a>View Details</a>
    <div class="photo" role="img" aria-label="Office building lit up at dusk" style="background:linear-gradient(180deg,#2f6fc8,#1e3a6a 60%,#c88a3a)"></div>
    <p>I must explain to you how all this mistaken idea of denouncing pleasure and praising</p>
  </article>
  <article class="abs service-card" style="left:351px">
    <h3>Residential Lighting</h3><a>View Details</a>
    <div class="photo" role="img" aria-label="Garden rocks and plants with glowing globe lights" style="background:radial-gradient(circle at 60% 50%,#d9b070,#3a4a5a 55%,#1e2a36)"></div>
    <p>I must explain to you how all this mistaken idea of denouncing pleasure and praising</p>
  </article>
  <article class="abs service-card" style="left:614px">
    <h3>Landscape lighting</h3><a>View Details</a>
    <div class="photo" role="img" aria-label="Lit garden path at night" style="background:radial-gradient(ellipse at 50% 70%,#9a7a3a,#2e3a1e 60%,#141a10)"></div>
    <p>I must explain to you how all this mistaken idea of denouncing pleasure and praising</p>
  </article>
  <article class="abs service-card" style="left:877px">
    <h3>Fiber Optic Installation</h3><a>View Details</a>
    <div class="photo" role="img" aria-label="Cable reel beside an open trench in a field" style="background:linear-gradient(120deg,#8a9a6a,#5a7a3a 50%,#6a5a3a)"></div>
    <p>I must explain to you how all this mistaken idea of denouncing pleasure and praising</p>
  </article>

  <div class="btn" style="left:463px;top:1849px;width:128px;height:43px">View More</div>
  <div class="btn" style="left:608px;top:1849px;width:129px;height:43px;background:var(--btn-grey)">Get Started</div>
</section>

<section>
  <div class="abs gallery-side-l" role="img" aria-label="Lit garden lamp by a pool"></div>
  <div class="abs gallery-main" role="img" aria-label="Stone garden pond with glowing underwater lights at dusk"></div>
  <div class="abs gallery-side-r" role="img" aria-label="House exterior with path lights"></div>
</section>

<section>
  <h2 class="abs section-title" style="top:2578px">Subscribe To Our Newsletter</h2>
  <p class="abs section-lead" style="top:2645px;left:150px;width:900px">I must explain to you how all this mistaken idea of denouncing pleasure and praising pain was born and I will give you a complete account of the system, and expound the actual teachings of the great explorer of the truth, the master-builder of human</p>
  <div class="abs subscribe"><span>Enter Email Address</span><div class="btn">Subscribe Now</div></div>
</section>

<footer class="abs footer">
  <div class="abs brand"><i></i>Halvern Ditchworks LTD</div>
  <nav class="abs footer-nav"><span>About Us</span><span>Irrigation Installs</span><span>Service</span><span>Landscape Lighting</span><span>Fiber Optic Installation</span></nav>
  <div class="abs footer-social"><span></span><span></span><span></span><span></span></div>
  <div class="abs copyright">(C) Copyright 2024 | All Rights Reserved</div>
</footer>

</body>
</html>
```